Business Card Design

We are a commercial real estate brokerage in San Francisco, leasing office buildings downtown.
I would like a clean, elegant look. Simple but powerful .

Industry/Entity Type

Business

Contact Information for Business Card

Derek Hollings
lic# 02875140
415.287.6041
derek@vexa-commercial.com
vexa-commercial.com

```html
<!DOCTYPE html>
<html lang="en">
<head>
<meta charset="utf-8">
<title>Vexa Commercial — Business Card</title>
<link rel="stylesheet" href="https://fonts.googleapis.com/css2?family=Oswald:wght@700&family=Source+Sans+3:wght@400;600&display=swap">
<style>
  :root {
    --brand-blue: #0096d8;
    --band-sky: #6dc8f0;
    --band-pale: #96caec;
    --band-grey: #b4b4b4;
    --band-light: #d1d1d1;
    --panel: #f0f1f3;
    --panel-edge: #d9ecf7;
    --brand-ink: #ffffff;
    --ink: #111111;
    --rule-dark: #4a4a4a;
  }
  html, body {
    margin: 0;
    padding: 0;
    width: 1200px;
    height: 702px;
    overflow: hidden;
    background: #ffffff;
  }
  .card {
    position: relative;
    width: 1200px;
    height: 702px;
    overflow: hidden;
    font-family: "Source Sans 3", "Myriad Pro", Arial, sans-serif;
  }
  .card__backdrop {
    position: absolute;
    inset: 0;
    display: block;
  }
  .brand {
    position: absolute;
    left: 92px;
    top: 112px;
    display: flex;
    align-items: center;
    gap: 18px;
    color: var(--brand-ink);
    font-weight: 600;
    font-size: 48px;
    line-height: 1;
    white-space: nowrap;
  }
  .brand__mark {
    width: 26px;
    height: 26px;
    border-radius: 50%;
    background: var(--brand-ink);
  }
  .contact {
    position: absolute;
    right: 80px;
    top: 254px;
    width: 520px;
    text-align: right;
    color: var(--ink);
  }
  .contact__name {
    margin: 0;
    font-family: "Oswald", "Franklin Gothic Demi Cond", sans-serif;
    font-weight: 700;
    font-size: 48px;
    line-height: 54px;
    letter-spacing: 0.3px;
  }
  .contact__rule {
    display: flex;
    width: 468px;
    height: 5px;
    margin: 22px 0 34px auto;
  }
  .contact__rule-accent { width: 160px; background: var(--brand-blue); }
  .contact__rule-base { flex: 1; background: var(--rule-dark); }
  .contact__list {
    list-style: none;
    margin: 0;
    padding: 0;
    font-size: 42px;
    line-height: 53px;
    white-space: nowrap;
  }
</style>
</head>
<body>
  <main class="card">
    <svg class="card__backdrop" width="1200" height="702" viewBox="0 0 1200 702" aria-hidden="true">
      <rect x="0" y="0" width="700" height="231" fill="var(--brand-blue)"/>
      <rect x="0" y="231" width="700" height="46" fill="var(--band-sky)"/>
      <rect x="0" y="277" width="700" height="190" fill="var(--band-pale)"/>
      <rect x="0" y="467" width="700" height="47" fill="var(--band-grey)"/>
      <rect x="0" y="514" width="700" height="188" fill="var(--band-light)"/>
      <polygon points="620,0 1200,0 1200,702 340,702" fill="var(--panel-edge)"/>
      <polygon points="634,0 1200,0 1200,702 356,702" fill="var(--panel)"/>
    </svg>

    <div class="brand">
      <span class="brand__mark"></span>
      <span class="brand__name">Vexa Commercial</span>
    </div>

    <section class="contact">
      <h1 class="contact__name">Derek Hollings</h1>
      <div class="contact__rule"><span class="contact__rule-accent"></span><span class="contact__rule-base"></span></div>
      <ul class="contact__list">
        <li>lic# 02875140</li>
        <li>415.287.6041</li>
        <li>derek@vexa-commercial.com</li>
        <li>vexa-commercial.com</li>
      </ul>
    </section>
  </main>
</body>
</html>
```